Meadowlark Hall Yoga Facebook Design

"Practice Radiant Movement"

Foundational and sustainable yoga practice to cultivate growth through a variety of anatomy- informed movement patterns. Develop an informative and inspirational connection with the mind, body and spirit, through smart and integrated movement.

-I need a design that is happy and cheerful and attracts children and adults alike. I teach vinyassa based yoga that is sustainable and smart, kid yoga, and chair yoga.

-A movement practic rooted in foundation, core, and expression

- Accessible yoga for a sustained practice. A guided movement practice where one gains information and knowledge of oneself through a mind/body connection. For one feel good physically with a new awareness of their internal radiance that exists in all beings. Physical rejuvenation egnites a light and increases energy to flow through the physical body, which ultimately tranlates into works of kindness for others and out in the world.

Dana Whitford
Yoga Instructor
MD, Pediatrician
RYT-200
RCYT
Certified yoga teacher for adults and children

Full description:
What is the positioning or mission statement of your company? to guide individuals in a yoga-based safe and sustainable movement practice applicable to all ages and body types. Currently my focus is working with children in daycare and school settings, but my goal is to expand into private yoga practice for adults, and potentially as part of rented space in studios. I hope to find a way to work with children AND adults (so would love for logo to be appealing to both), but current focus is with children based on need and demand in the community. yoga for children also compliments my backround as a pediatrician/neonatologist, and I greatly miss interacting with children. I also want to emphasize a yoga/movement practice that is focused more on what one feels internally through movement. NOT what one looks like asthetically. I believe in removing all mirrors from yoga/movement practice. It should be an experience of movement/poses/yoga through appropriate cueing and education. It is not about the details of how far the knee should bend, or how high the leg should be. Focusing on foudation first, core, then core engagement and ultimately expression of poses/movements. A focus on strength, stability and mobility, not just flexibility, which is the common perception/association with yoga. I also want individuals to learn to be an advocate of their own health. Through guidance, I hope for individuals to connect with their body so they know themselves so well to be able to advocate for themselves in the modern healthcare world. This internal experience and connection is so essential in a world where modern medicine has become a business and it is all about making a dollar. the connection with patients is lost, and individuals need to learn to empower themselves and through their new found voice to be able to articulate what is wrong.
Does your company have a tagline or slogan that should be included with the logo? "Practice Radiant Movement"
What do you hope your company can be known for? Accessible yoga for a sustained practice. A guided movement practice where one gains information and knowledge of oneself through a mind/body connection. For one feel good physically with a new awareness of their internal radiance that exists in all beings. Physical rejuvenation egnites a light and increases energy to flow through the physical body, which ultimately tranlates into works of kindness for others and out in the world.
What color palettes might you prefer? why? love the colors currently chosen
Where will the logo be primarily used? initially business cards, but hopefully future websites, t-shirts, and potentially local magazine adds. Also starting with a small couple of banners for community events in the area. I currently practice as a nomad out of my car :)
Are there any elements you would prefer to see in the logo? Movement. A modern depiction of a human body/figure practicing movement. Hoping to avoid a stereotypical yoga pose per say, just because I want to people to think of it more of a movement practice with yoga roots. Modern yoga. There are elements of breathing and connecting with oneself through the flow of breath and movement, but I do not focus on the meditative/cerebral aspect of the yoga practice. What I teach is almost reaching a meditative state through movement. I personally don't practice, nor resonate with just seated meditation. just not my thing :)
In your opinion, what defines a well-designed logo? curiosity. enough info for individuals to think they know what it means, but want to know more. invokes curiosity, but not too abstract. Reproducible. not too complicated. I want also to invoke a community feel, so a design that appeals to all people within a community.
What is your preference in reference to icons, typography, spokespeople (characters), etc.? modern design. I love the idea of a logo for my purposes, to invoke a sense of movement from within. So not too static.
What words or icons must be included in the logo? movement with yoga roots.
What logos do you like and why? A representation, but not exact. I think some ambiguity is intriguing for others, and also memorable. I want it to be an artistic representation of movement/yoga
What logos do you dislike and why? too busy, too loud.
In your opinion, what is the primary purpose for a logo? association
Who is the primary target audience? (who is most likely to use your services/product?) Children and their parents, but ultimately to expand into teaching adults. I even have aspirations of prenatal and post-natal yoga. Potentially incorporating infants.
Who currently uses your product the most? n/a (working in schools/daycare currently. It is currently all volunteer)
Are you pleased with the range of people your company serves? n/a
Are you looking to expand, modify, or completely change your target audience? or will it remain the same? yes! expand into an adult audience.
How do you plan to focus on your target audience? currently by working through schools and daycares. hopefully ultimately through after school care programs and then offering kid yoga in an existing yoga studio (working on this with Q loft in Ridgeland, currently)
What are your main forms of advertising? word of mouth, schools, daycares. Happy kids talking to their parents about the yoga class they took and happy teachers :)
How do most customers find out about your company?
Which gender are you targeting? All genders! However, with kid yoga, often the maternal individual in the child's life is more involved with decision making as far as extracurricular activities

Target Market(s)

Adults, children and families interested in movement, wellness and fun

Font styles to use
Sans Serif

Requirements
Must have
• ***I meant to emphasize the that "S" figure in my logo is SOOO iimportant to me. My daughter designed it. please highlight the "S" figure if possible******
My logo and the phrase "practice radiant movement"
Same colors as my logo
Feel like movement and fun.
Attracts children and families
Incorporate pieces of my description somehow
Nice to have
• different yoga poses or figures in movement
abstract design
attacts all body types and genders
inclusive

Industry is yoga, movement, wellness
Should not have
• no darkness
want happy and vibrant, inviting

```html
<!DOCTYPE html>
<html lang="en">
<head>
<meta charset="utf-8">
<title>Meadowlark Hall Yoga – Dana Whitford</title>
<link href="https://fonts.googleapis.com/css2?family=Montserrat:wght@400;500;700&family=Raleway:ital,wght@1,200&display=swap" rel="stylesheet">
<style>
  :root {
    --orange: #ef7b0b;
    --orange-deep: #e8600c;
    --amber: #f8a808;
    --yellow: #fde000;
    --gold: #fcc500;
    --red: #d8221e;
    --red-dark: #b81c1a;
    --cream: #fbefc8;
    --blue: #3d8fd6;
    --ink: #2a2522;
    --white: #ffffff;
  }
  html, body { margin: 0; padding: 0; overflow: hidden; background: #ffffff; }
  .poster {
    position: relative;
    width: 1200px;
    height: 811px;
    overflow: hidden;
    font-family: "Montserrat", Arial, sans-serif;
    color: var(--ink);
    background: linear-gradient(180deg, var(--orange) 0%, var(--orange) 40%, var(--amber) 62%, var(--gold) 82%, var(--yellow) 100%);
  }
  .waves { position: absolute; inset: 0; width: 1200px; height: 811px; }
  .headline {
    position: absolute;
    left: 216px;
    top: 2px;
    margin: 0;
    font-family: "Raleway", Arial, sans-serif;
    font-style: italic;
    font-weight: 200;
    font-size: 60px;
    letter-spacing: 0.5px;
    color: var(--white);
    white-space: nowrap;
  }
  .photo {
    position: absolute;
    border-radius: 50%;
    border: 2px solid var(--white);
    box-sizing: border-box;
  }
  .photo--poolside {
    left: 79px; top: 140px; width: 406px; height: 429px;
    background: radial-gradient(circle at 50% 35%, #6b5a58 0%, #7d7a6c 35%, #5d6b63 60%, #6fa3b4 85%);
  }
  .photo--garden {
    left: 454px; top: 222px; width: 379px; height: 380px;
    background: radial-gradient(circle at 50% 40%, #6f7a5d 0%, #4d5e3c 45%, #8a7c80 75%, #9a9692 100%);
  }
  .photo--outdoor-class {
    left: 827px; top: 312px; width: 336px; height: 336px;
    background: radial-gradient(circle at 50% 30%, #8dbf4e 0%, #5f9a3a 40%, #8b5a40 75%, #a86a4a 100%);
  }
  .brand {
    position: absolute;
    left: 890px;
    top: 118px;
    width: 270px;
    margin: 0;
    font-weight: 500;
    font-size: 28px;
    line-height: 1.15;
    color: var(--white);
    text-align: center;
  }
  .instructor {
    position: absolute;
    left: 25px;
    top: 652px;
  }
  .instructor__name {
    margin: 0;
    font-weight: 700;
    font-size: 40px;
    line-height: 1;
    letter-spacing: 0.5px;
    color: var(--red-dark);
  }
  .instructor__role {
    margin: 10px 0 0 2px;
    font-weight: 700;
    font-size: 25px;
    line-height: 1.1;
  }
  .instructor__credentials {
    margin: 2px 0 0;
    font-weight: 400;
    font-size: 25px;
    line-height: 1.15;
  }
  .offer {
    position: absolute;
    left: 379px;
    top: 720px;
    width: 400px;
    margin: 0;
    text-align: center;
    font-weight: 400;
    font-size: 28px;
    line-height: 1.16;
  }
  .contact {
    position: absolute;
    right: 26px;
    top: 726px;
    margin: 0;
    padding: 0;
    list-style: none;
    text-align: right;
    font-size: 18px;
  }
  .contact__item {
    display: flex;
    justify-content: flex-end;
    align-items: center;
    gap: 8px;
    height: 29px;
  }
  .contact__icon {
    width: 21px; height: 21px; border-radius: 50%;
    background: var(--white);
    display: flex; align-items: center; justify-content: center;
  }
</style>
</head>
<body>
<main class="poster">
  <svg class="waves" viewBox="0 0 1200 811" aria-hidden="true">
    <path d="M0 82 C250 62 520 110 760 170 C950 215 1080 215 1200 200 L1200 228 C1080 250 950 255 760 222 C520 170 260 120 0 136 Z" fill="var(--yellow)"/>
    <path d="M0 132 C260 115 520 165 760 222 C950 258 1080 255 1200 228 L1200 282 C1080 312 950 318 760 285 C520 240 260 200 0 210 Z" fill="var(--red)"/>
    <path d="M0 148 C260 132 520 180 760 236 C950 272 1080 268 1200 240" fill="none" stroke="var(--red-dark)" stroke-width="10" opacity="0.6"/>
    <path d="M0 210 C260 200 520 240 760 285 C950 320 1080 316 1200 282 L1200 298 C1080 334 950 340 760 304 C520 260 260 222 0 230 Z" fill="var(--white)" opacity="0.9"/>
    <path d="M0 230 C260 222 520 262 760 304 C950 340 1080 334 1200 298 L1200 326 C1080 360 950 366 760 330 C520 290 260 260 0 260 Z" fill="var(--gold)" opacity="0.7"/>
    <path d="M0 590 C220 560 460 555 700 575 C900 592 1060 640 1200 660 L1200 700 C1060 690 900 650 700 632 C460 610 220 615 0 640 Z" fill="var(--orange-deep)"/>
    <path d="M0 612 C220 585 460 582 700 600 C900 615 1060 660 1200 680 L1200 722 C1060 708 900 672 700 656 C460 640 220 640 0 650 Z" fill="var(--red)"/>
    <path d="M0 650 C220 640 460 642 700 658 C900 672 1060 708 1200 722 L1200 740 C1060 730 900 700 700 686 C460 672 220 672 0 676 Z" fill="var(--orange)" opacity="0.8"/>
    <g fill="none">
      <ellipse cx="276" cy="352" rx="244" ry="246" stroke="#f2b49a" stroke-width="3"/>
      <ellipse cx="272" cy="358" rx="236" ry="242" stroke="var(--red-dark)" stroke-width="4" opacity="0.7"/>
      <ellipse cx="274" cy="360" rx="226" ry="232" stroke="#8a8480" stroke-width="3"/>
      <ellipse cx="642" cy="412" rx="222" ry="208" stroke="var(--cream)" stroke-width="4"/>
      <ellipse cx="646" cy="416" rx="214" ry="202" stroke="#f3e2a0" stroke-width="3"/>
      <ellipse cx="995" cy="480" rx="190" ry="186" stroke="var(--blue)" stroke-width="3"/>
      <ellipse cx="991" cy="484" rx="182" ry="180" stroke="var(--orange-deep)" stroke-width="3"/>
    </g>
  </svg>

  <h1 class="headline">the best fitness studios</h1>

  <div class="photo photo--poolside" role="img" aria-label="Photo: instructor and two children in tree pose beside a backyard pool"></div>
  <div class="photo photo--garden" role="img" aria-label="Photo: instructor and two children seated in a garden doing a boat pose"></div>
  <div class="photo photo--outdoor-class" role="img" aria-label="Photo: outdoor kids yoga class on rugs under large trees"></div>

  <p class="brand">Meadowlark Hall Yoga</p>

  <section class="instructor">
    <h2 class="instructor__name">DANA WHITFORD</h2>
    <p class="instructor__role">Yoga Instructor</p>
    <p class="instructor__credentials">RYT-200, RCYT<br>Pediatrician</p>
  </section>

  <p class="offer">Certified Yoga Teacher<br>For Adults And Children</p>

  <ul class="contact">
    <li class="contact__item">555-014-2276
      <span class="contact__icon">
        <svg width="12" height="12" viewBox="0 0 24 24" aria-hidden="true"><path d="M6.6 10.8a15 15 0 0 0 6.6 6.6l2.2-2.2a1 1 0 0 1 1-.25 11.4 11.4 0 0 0 3.6.57 1 1 0 0 1 1 1V20a1 1 0 0 1-1 1A17 17 0 0 1 3 4a1 1 0 0 1 1-1h3.5a1 1 0 0 1 1 1c0 1.25.2 2.45.57 3.57a1 1 0 0 1-.25 1z" fill="var(--ink)"/></svg>
      </span>
    </li>
    <li class="contact__item">dana.whitford@example.com
      <span class="contact__icon">
        <svg width="12" height="12" viewBox="0 0 24 24" aria-hidden="true"><path d="M3 5h18v14H3z" fill="var(--ink)"/><path d="M3 6l9 7 9-7" fill="none" stroke="var(--white)" stroke-width="2"/></svg>
      </span>
    </li>
  </ul>
</main>
</body>
</html>
```